I am medical doctor in surgery specialized in Urology and anti-aging. I need Web and Instagram design for a head cream , face cream and body lotion. I did a 2% GHK-Cu solution (head-face-body) with an professional pharmacist specialized in manufacturing creams. . GHK-Cu is a tri-peptide with solid scientific background to rejuvenate the skin (will stimulate collagen production) and can promote hair regrowth. Statistically 70% of peptides bought are fake on the market, I can personally guarantee about purity (my peptides are certified pure above 99% checked in an independent laboratory in London -UK.
I want to use the name 'Lunavel'. I secured already the domain names. I had an design for another project I could re-use for this project. The ribbon should include more blue. The font of Lunavel can be changed. I got a logo which is ok for me. Web design best coded with Wordpress.

Target Market(s)

Anti aging, skin care, hair regrowth, skin collagen

Industry/Entity Type

the cream can also be used after surgery for faster and better wound healing

Number of Pages Required

5+ page

Font styles to use
Sans Serif

Colors
0054AA
0677BA
7BADD7
CADEEF
E8F1F8

Requirements
Must have
• target population 30-70 years
Nice to have
• scientific proof, pictures before-after
Should not have
• GHK-Cu has solid scientific animal studies of anti-cancer properties. It is 100% safe for dermal human use.

```html
<!DOCTYPE html>
<html lang="en">
<head>
<meta charset="utf-8">
<title>Lunavel — GHK-Cu Peptide Rejuvenation</title>
<link href="https://fonts.googleapis.com/css2?family=Oswald:wght@500;600;700&family=Poppins:wght@400;500;600&display=swap" rel="stylesheet">
<style>
:root{
  --navy:#0054AA;
  --blue:#0677BA;
  --brand:#1a7cc9;
  --sky:#7BADD7;
  --mist:#CADEEF;
  --ice:#E8F1F8;
  --ink:#1b1b1b;
  --dark:#2b2b2b;
  --footer:#232323;
  --grey:#666;
  --line:#e3e3e3;
  --star:#f2b619;
}
*{box-sizing:border-box;margin:0;padding:0}
html,body{width:1200px;height:3876px;overflow:hidden}
body{position:relative;background:#fff;font-family:"Poppins",sans-serif;color:var(--ink)}
.abs{position:absolute}
.heading{font-family:"Oswald",sans-serif;font-weight:700;text-transform:uppercase;letter-spacing:.5px;color:var(--ink)}
.center{left:0;width:1200px;text-align:center}
.btn-pill{position:absolute;display:flex;align-items:center;justify-content:center;border-radius:20px;font-family:"Oswald",sans-serif;font-weight:600;font-size:13px;text-transform:uppercase;background:var(--navy);color:#fff;letter-spacing:.3px}

/* top bar */
.topbar{left:0;top:0;width:1200px;height:38px;background:var(--dark);color:#eee;font-size:12px;display:flex;align-items:center;justify-content:center;gap:8px}
/* header */
.logo{left:161px;top:62px}
.logo-name{font-family:"Poppins",sans-serif;font-weight:500;font-size:38px;color:#3a3a3a;line-height:1;display:flex;align-items:center;gap:8px}
.logo-name .dot{width:12px;height:12px;background:var(--brand);border-radius:50%}
.logo-tag{font-size:12px;letter-spacing:1.5px;color:#333;margin-top:6px}
.search{left:418px;top:72px;width:387px;height:36px;border:1px solid var(--line);border-radius:18px;display:flex;align-items:center;gap:10px;padding-left:16px;font-size:11px;color:#888}
.account{left:812px;top:72px;width:107px;height:36px;border:1.5px solid #333;border-radius:18px;display:flex;align-items:center;justify-content:center;gap:8px;font-size:12px;font-weight:500}
.cart{left:928px;top:72px;width:110px;height:36px;background:var(--brand);border-radius:18px;display:flex;align-items:center;justify-content:center;gap:8px;font-size:12px;font-weight:600;color:#fff}
.nav{left:0;top:146px;width:1200px;height:47px;border-top:1px solid #eee;border-bottom:1px solid #eee}
.nav a{position:absolute;top:16px;font-family:"Oswald",sans-serif;font-weight:500;font-size:13px;color:#222;text-decoration:none}
.nav a.active{color:var(--brand)}

/* hero */
.hero{left:0;top:193px;width:1200px;height:499px;background:linear-gradient(90deg,#6ea5d8 0%,#7bafdd 55%,#a9cbe9 100%);overflow:hidden}
.hero-photo{position:absolute;left:700px;top:0;width:500px;height:499px;background:linear-gradient(120deg,#dfe8f0 0%,#cdb8a6 55%,#9c7a62 100%);clip-path:polygon(18% 0,100% 0,100% 100%,0 100%)}
.hero-bottle{position:absolute;left:726px;top:78px;width:112px;height:323px;border-radius:30px 30px 14px 14px;background:linear-gradient(90deg,#e4ebf2,#fff 40%,#cfdcea);transform:rotate(8deg)}
.hero-eyebrow{left:161px;top:308px;font-size:17px;color:#fff;letter-spacing:.5px}
.hero-title{left:161px;top:332px;font-family:"Oswald",sans-serif;font-weight:700;font-size:56px;line-height:68px;color:#fff;text-transform:uppercase}
.hero-text{left:161px;top:466px;width:470px;font-size:13px;line-height:16px;color:#fff}
.hero-btn{left:161px;top:531px;width:159px;height:35px;background:#333;border-radius:18px}
.arrow{top:415px;width:42px;height:56px;background:rgba(120,140,160,.6);display:flex;align-items:center;justify-content:center}

/* bestsellers */
.best-card{top:833px;width:275px;height:251px;background:#fff;border-radius:10px;box-shadow:0 6px 24px rgba(0,40,90,.12)}
.best-card.blue{background:var(--brand)}
.best-kicker{position:absolute;left:25px;top:22px;font-family:"Oswald",sans-serif;font-weight:600;font-size:30px;color:#222}
.best-word{position:absolute;left:25px;top:50px;font-family:"Oswald",sans-serif;font-weight:700;font-size:66px;color:var(--ice);-webkit-text-stroke:2px var(--sky);letter-spacing:1px}
.blue .best-kicker{color:#fff}
.blue .best-word{color:var(--brand);-webkit-text-stroke:2px var(--mist)}
.pack{position:absolute;border-radius:12px;background:linear-gradient(90deg,#c9cfd6,#fff 45%,#b9c2cc)}

/* featured */
.prod{top:1316px;width:239px;height:386px;border:1px solid var(--line);border-radius:6px;background:#fff}
.stars{position:absolute;top:18px;left:0;width:100%;text-align:center;font-size:15px;color:var(--star)}
.stars span{font-size:11px;color:#444;margin-left:4px}
.prod-img{position:absolute;top:60px;border-radius:8px;background:linear-gradient(90deg,#c6ccd3,#fff 45%,#b8c1cb)}
.price{position:absolute;top:227px;left:97px;width:57px;height:23px;background:var(--blue);color:#fff;font-family:"Oswald",sans-serif;font-size:13px;display:flex;align-items:center;justify-content:center}
.prod-name{position:absolute;top:267px;left:0;width:100%;text-align:center;font-family:"Oswald",sans-serif;font-weight:600;font-size:25px}
.prod-btn{position:absolute;top:320px;left:28px;width:183px;height:35px;border:1.5px solid #222;border-radius:18px;display:flex;align-items:center;justify-content:center;font-family:"Oswald",sans-serif;font-weight:600;font-size:13px}
.dots{left:573px;top:1730px;display:flex;gap:6px}
.dots i{width:7px;height:7px;border-radius:50%;background:#bbb;display:block}
.dots i.on{background:var(--sky)}

/* technology */
.tech{left:0;top:1865px;width:1200px;height:403px;background:linear-gradient(90deg,#bcd3ea 0%,#d5e4f2 45%,#e8f1f8 100%);overflow:hidden}
.tech-photo{position:absolute;left:0;top:0;width:720px;height:403px;background:linear-gradient(110deg,#4f86c8 0%,#c9b2a1 35%,#e1d4c9 60%,rgba(210,226,241,0) 100%)}
.tech-title{left:750px;top:1960px;font-family:"Oswald",sans-serif;font-weight:700;font-size:56px;line-height:68px;color:#1b1b1b;text-transform:uppercase}
.tech-text{left:753px;top:2104px;width:320px;font-size:13px;line-height:16px;color:#333}

/* before after */
.ba{top:2402px;width:299px;height:238px}
.ba-half{position:absolute;top:0;width:148px;height:238px}
.ba-tag{position:absolute;top:0;height:22px;width:148px;font-family:"Oswald",sans-serif;font-size:12px;font-weight:600;color:#fff;display:flex;align-items:center;justify-content:center;letter-spacing:.5px}
.ba-quote{position:absolute;left:126px;top:216px;width:48px;height:48px;border-radius:50%;background:#fff;display:flex;align-items:center;justify-content:center;font-family:"Oswald",sans-serif;font-size:34px;font-weight:700;color:var(--brand);line-height:1;padding-top:12px}
.review{top:2676px;width:310px;text-align:center}
.review h4{font-weight:500;font-size:16px;color:#333;letter-spacing:.3px}
.review p{font-size:11px;line-height:14px;color:#555;margin-top:12px}
.review .who{font-size:11px;color:#555;margin-top:14px}

/* why choose */
.why{left:161px;top:2889px;width:877px;height:308px}
.why-title{top:2930px;font-family:"Oswald",sans-serif;font-weight:700;font-size:36px;color:#fff}
.why-text{top:2987px;font-size:15px;line-height:19px;color:#fff}
.feat{display:flex;align-items:center;gap:10px;font-family:"Oswald",sans-serif;font-weight:600;font-size:21px;color:#fff;line-height:25px}

/* story */
.story-title{top:3252px;font-family:"Oswald",sans-serif;font-weight:700;font-size:38px}
.story-text{left:253px;top:3333px;width:695px;text-align:center;font-size:14px;line-height:19.5px;color:#444}

/* footer */
.footer{left:0;top:3593px;width:1200px;height:283px;background:var(--footer)}
.news-title{left:161px;top:3625px;font-family:"Oswald",sans-serif;font-weight:600;font-size:19px;color:#fff}
.news-sub{left:161px;top:3654px;font-size:11px;color:#ddd}
.news-input{left:600px;top:3629px;width:337px;height:41px;background:#fff;border-radius:20px 0 0 20px;font-size:11px;color:#888;display:flex;align-items:center;padding-left:14px}
.news-btn{left:937px;top:3629px;width:101px;height:41px;background:var(--brand);border-radius:0 20px 20px 0;color:#fff;font-size:12px;font-weight:600;display:flex;align-items:center;justify-content:center}
.flinks a{position:absolute;top:3745px;font-size:15px;color:#fff;text-decoration:none}
.social{top:3746px;width:16px;height:16px;border-radius:50%;border:2px solid #fff}
.pay{top:3827px;width:42px;height:30px;border-radius:3px}
</style>
</head>
<body>

<div class="abs topbar">
  <svg width="14" height="14" viewBox="0 0 24 24" fill="#fff"><path d="M6.6 10.8a15 15 0 0 0 6.6 6.6l2.2-2.2a1 1 0 0 1 1-.25 11 11 0 0 0 3.6.57 1 1 0 0 1 1 1V20a1 1 0 0 1-1 1A17 17 0 0 1 3 4a1 1 0 0 1 1-1h3.5a1 1 0 0 1 1 1c0 1.25.2 2.45.57 3.57a1 1 0 0 1-.25 1z"/></svg>
  Questions? 085-0123456
</div>

<header>
  <div class="abs logo">
    <div class="logo-name">Lunavel<span class="dot"></span></div>
    <div class="logo-tag">PEPTIDE REJUVENATION</div>
  </div>
  <div class="abs search">
    <svg width="14" height="14" viewBox="0 0 24 24" fill="none" stroke="#333" stroke-width="2.5"><circle cx="10" cy="10" r="7"/><path d="M15 15l6 6"/></svg>
    Search for...
  </div>
  <div class="abs account">
    <svg width="14" height="14" viewBox="0 0 24 24" fill="none" stroke="#222" stroke-width="2"><circle cx="12" cy="8" r="4"/><path d="M4 21c1-4 4-6 8-6s7 2 8 6"/></svg>
    Account
  </div>
  <div class="abs cart">
    <svg width="16" height="16" viewBox="0 0 24 24" fill="none" stroke="#fff" stroke-width="2"><path d="M2 3h3l2.5 12h11L21 7H6"/><circle cx="9" cy="20" r="1.5"/><circle cx="18" cy="20" r="1.5"/></svg>
    $0.00 (0)
  </div>
  <nav class="abs nav">
    <a class="active" style="left:300px">HOME</a>
    <a style="left:406px">PRODUCTS &#8964;</a>
    <a style="left:530px">GHK-CU</a>
    <a style="left:636px">RESULTS</a>
    <a style="left:747px">ABOUT</a>
    <a style="left:847px">CONTACT</a>
  </nav>
</header>

<section class="abs hero">
  <div class="hero-photo" role="img" aria-label="Woman applying cream to her cheek"></div>
  <div class="hero-bottle" role="img" aria-label="Lunavel GHK-Cu body lotion bottle"></div>
</section>
<div class="abs hero-eyebrow">ANTI-AGING SKINCARE</div>
<h1 class="abs hero-title">Healthy Skin Starts<br>With Science</h1>
<p class="abs hero-text">Premium GHK-Cu formulations designed to nourish, repair, and rejuvenate skin while supporting natural collagen production and a radiant complexion.</p>
<div class="btn-pill hero-btn">Shop Now</div>
<div class="abs arrow" style="left:0"><svg width="14" height="20" viewBox="0 0 14 20" fill="none" stroke="#fff" stroke-width="2"><path d="M11 2L3 10l8 8"/></svg></div>
<div class="abs arrow" style="left:1158px"><svg width="14" height="20" viewBox="0 0 14 20" fill="none" stroke="#fff" stroke-width="2"><path d="M3 2l8 8-8 8"/></svg></div>

<h2 class="abs heading center" style="top:740px;font-size:40px">Our Bestsellers</h2>

<div class="abs best-card" style="left:161px">
  <div class="best-kicker">FACE</div><div class="best-word">CREAM</div>
</div>
<div class="pack" role="img" aria-label="Face cream jar" style="left:220px;top:990px;width:158px;height:185px"></div>
<div class="abs best-card" style="left:462px">
  <div class="best-kicker">BODY</div><div class="best-word">LOTION</div>
</div>
<div class="pack" role="img" aria-label="Body lotion bottle" style="left:560px;top:965px;width:72px;height:238px;border-radius:24px 24px 10px 10px;transform:rotate(6deg)"></div>
<div class="abs best-card blue" style="left:763px">
  <div class="best-kicker">HAIR</div><div class="best-word">CREAM</div>
  <svg class="abs" style="left:228px;top:208px" width="30" height="24" viewBox="0 0 30 24" fill="none" stroke="#cadeef" stroke-width="1.5"><path d="M4 14c3-1 5 2 7 3l1-13c0-2 3-2 3 0v8l9 2c2 1 2 3 1 5l-2 4H12L4 16z"/></svg>
</div>
<div class="pack" role="img" aria-label="Hair cream bottle" style="left:866px;top:970px;width:60px;height:230px;border-radius:22px 22px 10px 10px;transform:rotate(10deg)"></div>

<h2 class="abs heading center" style="top:1230px;font-size:40px">Featured Products</h2>

<div class="abs prod" style="left:96px">
  <div class="stars">★★★★★<span>(10)</span></div>
  <div class="prod-img" role="img" aria-label="Face cream jar" style="left:66px;width:107px;height:125px;top:70px"></div>
  <div class="price">$80.60</div><div class="prod-name">Face Cream</div><div class="prod-btn">Add To Cart</div>
</div>
<div class="abs prod" style="left:352px">
  <div class="stars">★★★★★<span>(10)</span></div>
  <div class="prod-img" role="img" aria-label="Body lotion bottle" style="left:100px;width:40px;height:152px;border-radius:14px 14px 6px 6px"></div>
  <div class="price">$80.60</div><div class="prod-name">Body Lotion</div><div class="prod-btn">Add To Cart</div>
</div>
<div class="abs prod" style="left:608px">
  <div class="stars">★★★★★<span>(10)</span></div>
  <div class="prod-img" role="img" aria-label="Hair cream bottle" style="left:103px;width:34px;height:152px;border-radius:12px 12px 6px 6px"></div>
  <div class="price">$50.60</div><div class="prod-name">Hair Cream</div><div class="prod-btn">Add To Cart</div>
</div>
<div class="abs prod" style="left:863px">
  <div class="stars">★★★★★<span>(10)</span></div>
  <div class="prod-img" role="img" aria-label="Anti aging cream jar" style="left:66px;width:107px;height:125px;top:70px"></div>
  <div class="price">$90.60</div><div class="prod-name">Anti Aging</div><div class="prod-btn">Add To Cart</div>
</div>
<div class="abs dots"><i></i><i></i><i class="on"></i><i></i></div>
<div class="btn-pill" style="left:513px;top:1770px;width:174px;height:32px">View All Products</div>

<section class="abs tech">
  <div class="tech-photo" role="img" aria-label="Smiling woman with Lunavel serum bottles and molecule graphics"></div>
</section>
<h2 class="abs tech-title">GHK-CU<br>Technology</h2>
<p class="abs tech-text">Quality peptide products from trusted Valley farms, third-party tested for purity.</p>
<div class="btn-pill" style="left:753px;top:2163px;width:160px;height:33px">Shop Now</div>

<h2 class="abs heading center" style="top:2315px;font-size:40px">Before After</h2>

<div class="abs ba" style="left:140px">
  <div class="ba-half" role="img" aria-label="Skin before treatment" style="left:0;background:linear-gradient(135deg,#a47b62,#7a5a47)"></div>
  <div class="ba-half" role="img" aria-label="Skin after treatment" style="left:151px;background:linear-gradient(135deg,#caa287,#8e6a52)"></div>
  <div class="ba-tag" style="left:0;background:#777">BEFORE</div><div class="ba-tag" style="left:151px;background:var(--brand)">AFTER</div>
  <div class="ba-quote">&#8220;</div>
</div>
<div class="abs ba" style="left:450px">
  <div class="ba-half" role="img" aria-label="Scalp before treatment" style="left:0;background:linear-gradient(135deg,#8a6c5c,#3a2a22)"></div>
  <div class="ba-half" role="img" aria-label="Scalp after treatment" style="left:151px;background:linear-gradient(135deg,#6b5a50,#2a2220)"></div>
  <div class="ba-tag" style="left:0;background:#777">BEFORE</div><div class="ba-tag" style="left:151px;background:var(--brand)">AFTER</div>
  <div class="ba-quote">&#8220;</div>
</div>
<div class="abs ba" style="left:754px">
  <div class="ba-half" role="img" aria-label="Skin before treatment" style="left:0;background:linear-gradient(135deg,#d7a890,#9c6c58)"></div>
  <div class="ba-half" role="img" aria-label="Skin after treatment" style="left:151px;background:linear-gradient(135deg,#e3c0ac,#a47a64)"></div>
  <div class="ba-tag" style="left:0;background:#777">BEFORE</div><div class="ba-tag" style="left:151px;background:var(--brand)">AFTER</div>
  <div class="ba-quote">&#8220;</div>
</div>
<div class="abs review" style="left:135px"><h4>Smoother, Brighter Skin</h4><p>Fine lines appeared softer, and my skin feels smoother and more radiant after consistent use.</p><div class="who">— Clara D</div></div>
<div class="abs review" style="left:445px"><h4>Clearer, Healthier Skin</h4><p>My skin feels more balanced, hydrated, and The texture has noticeably improved.</p><div class="who">— Mark T</div></div>
<div class="abs review" style="left:749px"><h4>Clearer, Healthier Skin</h4><p>My skin feels more balanced, hydrated, and The texture has noticeably improved.</p><div class="who">— Mark T</div></div>
<div class="btn-pill" style="left:528px;top:2808px;width:144px;height:33px">View All</div>

<svg class="abs why" viewBox="0 0 877 308" aria-hidden="true">
  <path d="M0 0H877V308L438.5 232 0 308Z" fill="var(--brand)"/>
  <path d="M10 10H867V280L438.5 214 10 280Z" fill="none" stroke="#fff" stroke-width="2"/>
  <path d="M0 296L438.5 222 877 296" fill="none" stroke="#fff" stroke-width="3"/>
</svg>
<h2 class="abs center why-title">WHY CHOOSE US</h2>
<p class="abs center why-text">We're here at Bloom House to ensure that you have the best possible<br>experience with the highest quality products.</p>
<div class="abs feat" style="left:216px;top:3086px">
  <svg width="64" height="36" viewBox="0 0 64 36" fill="#fff"><rect x="14" y="4" width="30" height="22" rx="2"/><path d="M44 10h10l8 9v7H44z"/><circle cx="24" cy="29" r="5"/><circle cx="52" cy="29" r="5"/><rect x="0" y="9" width="11" height="3"/><rect x="3" y="16" width="8" height="3"/></svg>
  Fast Delivery
</div>
<div class="abs feat" style="left:511px;top:3053px">
  <svg width="32" height="44" viewBox="0 0 32 44" fill="none" stroke="#fff" stroke-width="3"><circle cx="16" cy="14" r="11"/><path d="M9 24l-4 17 11-6 11 6-4-17"/><path d="M16 8l2 4 4 .5-3 3 1 4-4-2-4 2 1-4-3-3 4-.5z" fill="#fff" stroke="none"/></svg>
  High-Qality Feed
</div>
<div class="abs feat" style="left:814px;top:3072px">
  <svg width="42" height="46" viewBox="0 0 42 46" fill="#fff"><circle cx="21" cy="8" r="7"/><path d="M2 44c0-12 7-20 14-20h4v20z"/><path d="M26 22l14 5v7c0 6-6 10-14 12-8-2-0-6 0-12z" fill="none"/><path d="M24 24l14 4v7c0 5-6 9-14 11z"/></svg>
  Trusted By<br>Professionals
</div>

<h2 class="abs heading center story-title">Clinically Inspired. Scientifically Crafted</h2>
<p class="abs story-text">Lunavel combines advanced peptide technology with thoughtfully selected ingredients to create premium skincare solutions for face, body, and hair. Our commitment to quality, innovation, and daily skin wellness ensures every formula is designed to support healthier-looking skin through consistent care. Healthy skin starts with trusted science. Lunavel harnesses the power of GHK-Cu peptide in carefully developed formulations that help nourish, hydrate, and support smoother, more radiant-looking skin. Designed with quality and innovation in mind, our products fit seamlessly into your everyday skincare routine.</p>
<div class="btn-pill" style="left:513px;top:3498px;width:174px;height:34px">Learn More</div>

<footer class="abs footer"></footer>
<div class="abs news-title">SIGN UP FOR OUR NEWSLETTER</div>
<div class="abs news-sub">Give your inbox some love with new products tips, &amp; more.</div>
<div class="abs news-input">Enter Email Address</div>
<div class="abs news-btn">SUBSCRIBE</div>
<div class="flinks">
  <a style="left:161px">Home</a><a style="left:245px">Shop</a><a style="left:323px">About Us</a><a style="left:430px">Science</a><a style="left:529px">GHK-Cu</a><a style="left:630px">Before &amp; After</a><a style="left:773px">Contact Us</a>
</div>
<div class="abs social" style="left:936px"></div>
<div class="abs social" style="left:978px"></div>
<div class="abs social" style="left:1021px"></div>
<div class="abs pay" style="left:502px;background:var(--navy)"></div>
<div class="abs pay" style="left:553px;background:var(--blue)"></div>
<div class="abs pay" style="left:605px;background:#444"></div>
<div class="abs pay" style="left:656px;background:var(--brand)"></div>

</body>
</html>
```